Clean Chic Simple Black & White One sided Biz Card

I need a business card for my company Brightwater Docket Partners. We are a luxury, white glove service for organizing files for attorneys.
I would like something that is stunningly simple and chic/sexy. This is going to be only one sided. We are going to use raised ink or ink embossing for the printing. So the logo will be raised in black. I am currently waiting to hear back from the printer as to whether or not the logo has to be in all black or can be left in its current state of black with grey initials. Please check our website for inspiration. www.brightwaterdocketpartners.example.
Thank you so much for your time.

* Please decide whichever title you think looks best(Chief Executive Officer, CEO, or President)
Updates

I really like the designs that make the logo large and the main focus.  
I also like the use of modern, masculine, simple, chic fonts for the slogan and info.

1) No bold font on slogan or info
2) Shrink info to be smaller maybe to make the logo bigger and more the focus
3) Maybe use grey for all the info and slogan so the focus will be on the logo

Thank you so much for your time!!

Target Market(s)

Luxury driven lawyers and their support staff

Industry/Entity Type

Printer

Requirements
Must have
• One sided card

Modern, sleek, masculine, chic, simple font.

Please add our slogan. Refer to file labeled "old logo" to see how we added our slogan under the old logo.
The slogan is, "Every Brief in Its Proper Place"

Please include the info below:
Marina Thornbury (Chief Executive Officer, CEO, or President)
812 North Delmont Avenue, Suite 1400
Los Angeles, California 90017
P: (213)555-0186 F: (213)555-0142
marinat@brightwaterdocketpartners.example
www.brightwaterdocketpartners.example

Please refer to attached file labeled "inkpressingembossing requirements" for requirements from my printer. Thank you!
Nice to have
• It can be super simple with just the logo and my info. Or it could maybe have some cool feature. Just clean please.

I would prefer the info not be in bold. I think this will help the Logo stand out as the main focus.

I attached files of how the ink pressing and embossing will look.
Should not have
• No crazy shapes and no color other than black with a white background. The logo should be the focus since it will be embossed.

```html
<!DOCTYPE html>
<html lang="en">
<head>
<meta charset="utf-8">
<title>Brightwater Docket Partners – Business Card</title>
<link rel="stylesheet" href="https://fonts.googleapis.com/css2?family=Pathway+Gothic+One&family=Playfair+Display:wght@800&display=swap">
<style>
  :root {
    --ink: #111111;
    --paper: #ffffff;
    --accent-grey: #a7b4b7;
    --text-grey: #2a2a2a;
  }
  html, body {
    margin: 0;
    padding: 0;
    width: 1200px;
    height: 686px;
    overflow: hidden;
    background: var(--paper);
  }
  .card {
    position: relative;
    width: 1200px;
    height: 686px;
    background: var(--paper);
    font-family: "Pathway Gothic One", "Arial Narrow", sans-serif;
    color: var(--ink);
  }
  .brand-mark {
    position: absolute;
    left: 510px;
    top: 96px;
    width: 180px;
    height: 180px;
  }
  .company-name {
    position: absolute;
    left: 0;
    top: 298px;
    width: 1200px;
    margin: 0;
    text-align: center;
    white-space: nowrap;
    font-family: "Playfair Display", Georgia, serif;
    font-size: 33px;
    font-weight: 800;
    letter-spacing: 5px;
    line-height: 1;
    text-transform: uppercase;
    color: var(--ink);
  }
  .slogan {
    position: absolute;
    left: 0;
    top: 348px;
    width: 1200px;
    margin: 0;
    text-align: center;
    font-size: 30px;
    letter-spacing: 1px;
    line-height: 1;
    text-transform: uppercase;
    color: var(--ink);
  }
  .address-block {
    position: absolute;
    right: 617px;
    top: 440px;
    text-align: right;
    font-style: normal;
    font-size: 22px;
    line-height: 34.5px;
    color: var(--text-grey);
    white-space: nowrap;
  }
  .divider {
    position: absolute;
    left: 600px;
    top: 432px;
    width: 4px;
    height: 156px;
    background: var(--ink);
  }
  .contact-block {
    position: absolute;
    left: 625px;
    top: 440px;
    font-size: 22px;
    line-height: 34.5px;
    color: var(--text-grey);
    white-space: nowrap;
  }
  .contact-block .person-name,
  .contact-block .person-title {
    font-size: 25px;
    text-transform: uppercase;
    color: var(--ink);
  }
  .address-block p, .contact-block p { margin: 0; }
</style>
</head>
<body>
  <main class="card">
    <svg class="brand-mark" viewBox="0 0 180 180" aria-hidden="true">
      <circle cx="90" cy="90" r="86" fill="var(--accent-grey)"/>
    </svg>

    <h1 class="company-name">Brightwater Docket Partners, Inc.</h1>
    <p class="slogan">"Every Brief in Its Proper Place"</p>

    <address class="address-block">
      <p>812 North Delmont Avenue, Suite 1400,</p>
      <p>Los Angeles, California 90017</p>
      <p>P: (213)555-0186</p>
      <p>F: (213)555-0142</p>
    </address>

    <div class="divider"></div>

    <div class="contact-block">
      <p class="person-name">Marina Thornbury</p>
      <p class="person-title">Chief Executive Officer</p>
      <p class="website">www.brightwaterdocketpartners.example</p>
      <p class="email">marinat@brightwaterdocketpartners.example</p>
    </div>
  </main>
</body>
</html>
```